To design a professional looking flyer for a mailbox drop.

On the front we would like the Loft logo, our email address (theloftcanberra@mailpinto.com) and A special offer
Sign on for six months get your first six weeks Free (saving of $302)
Sign on for three months get your first three weeks free (saving of $151)

On the back "5 things you can do NOW to look after your Mental Health''
1. Remain connected to supportive people. Spend time with and reach out to people who are a positive influence on you. Having a network of good relationships and taking part in social activities improves confidence, wellbeing and keeps our mind busy.
2. Be aware of negative thoughts. Thoughts arent necessarily facts and it can be easy to let our mind get away on us. Be aware of your negative thoughts and try not to give them power. Come up with a strategy so that when you notice yourself thinking negatively you can implement the strategy that overrides the thought, practice it regularly and overtime you’ll be the master of your mind, rather than your mind being the master of you!
3. Develop a daily routine that prioritises something you enjoy. Make YOU your non negotiable. We all lead busy lives, but its important to do something for ourselves that we enjoy and can look forward to. Taking a bath, coffee with a friend, a walk, reading before bed, gardening. Its nice to look back on your day and see we have done something for ourselves.
4. Exercise, movement is key! Daily exercise is best however, its been proven that as little as 45 mins of exercise three times a week can lessen feelings of depressions, anxiety and stress. Find something you enjoy doing, a gym class where the session is planned for you, walk in do your exercise, walk out and get on with your day, walking, running, dancing, just be sure to get it done. The benefits are endless. Gradually build it into your routine, exercise with a friend, it helps keep you both accountable and its more fun too!
5. Eat well. Our brain and gut are connected, this is known as the Gut Brain axis. Our GI tract releases neurotransmitters and hormones like serotonin and dopamine which affect brain function and mood. If the microbes in your gut are unbalanced it can lead to less production of the ‘happy hormones.’ Probiotics are key to balanced gut health, think probiotic yoghurts, kimchi, miso soup, sauerkraut or probiotic supplements. Vitamin D rich foods wil help too, eggs yolks, tuna, salmon. Lighten up on the sugary and processed food as these can inhibit the growth of good bacteria.

Industry/Entity Type

we are a gym

Colors

Designer to choose colors to be used in the design.

Requirements
Must have
• logo/s

```html
<!DOCTYPE html>
<html lang="en">
<head>
<meta charset="utf-8">
<title>The Loft Canberra – Mailbox Flyer</title>
<link href="https://fonts.googleapis.com/css2?family=Barlow:ital,wght@0,300;0,400;0,600;0,700;0,800;1,800&display=swap" rel="stylesheet">
<style>
  :root {
    --red: #ec1c24;
    --black: #0c0c0c;
    --panel: #1a1a1a;
    --white: #ffffff;
    --grey: #5a5a5a;
    --body: #e8e8e8;
    --rule: #6a6a6a;
  }
  * { margin: 0; padding: 0; box-sizing: border-box; }
  html, body { width: 1200px; height: 785px; overflow: hidden; background: var(--white); }
  body { position: relative; font-family: "Barlow", Arial, sans-serif; color: var(--white); }

  .page {
    position: absolute; top: 49px; width: 530px; height: 686px; overflow: hidden;
    background: radial-gradient(ellipse at 60% 40%, #2a2a2a 0%, #181818 55%, #0e0e0e 100%);
    box-shadow: 0 4px 18px rgba(0,0,0,0.35);
  }
  .front { left: 58px; }
  .back { left: 621px; }

  /* Front */
  .brand { position: absolute; top: 70px; left: 0; width: 100%; text-align: center; }
  .brand-lockup { display: inline-flex; align-items: center; gap: 12px; }
  .brand-mark { width: 70px; height: 70px; background: var(--red); }
  .brand-name { font-weight: 800; font-size: 64px; line-height: 1; letter-spacing: 1px; color: var(--white); }

  .burst { position: absolute; left: 184px; top: 200px; width: 140px; height: 100px; z-index: 3; }
  .burst-label {
    position: absolute; left: 184px; top: 222px; width: 140px; z-index: 4; text-align: center;
    font-weight: 800; font-style: italic; font-size: 19px; line-height: 20px; color: var(--black);
  }

  .offer { position: absolute; left: 70px; width: 376px; height: 111px; }
  .offer-frame { position: absolute; inset: -4px -8px -10px -8px; border: 4px solid var(--red); transform: rotate(1.6deg); }
  .offer-box { position: absolute; inset: 0; background: var(--black); border: 5px solid var(--red); }
  .offer-six { top: 281px; }
  .offer-three { top: 439px; }
  .offer-lead { position: absolute; top: 14px; font-weight: 300; font-size: 17px; line-height: 1; }
  .offer-big { position: absolute; top: 38px; font-weight: 700; font-size: 31px; line-height: 32px; }
  .offer-left { left: 19px; }
  .offer-right { left: 214px; }
  .offer-plus {
    position: absolute; left: 175px; top: 38px; width: 25px; height: 25px; background: var(--red);
    font-weight: 700; font-size: 26px; line-height: 22px; text-align: center;
  }
  .offer-saving {
    position: absolute; left: 14px; bottom: 0; width: 152px; height: 28px; background: var(--red);
    font-weight: 300; font-size: 17px; line-height: 28px; padding-left: 11px;
  }
  .offer-saving strong { font-weight: 700; }

  .front-slash { position: absolute; left: 0; top: 578px; width: 530px; height: 30px; }
  .front-contact {
    position: absolute; left: 0; top: 607px; width: 530px; height: 50px; background: var(--red);
    display: flex; align-items: center; justify-content: center; gap: 7px; font-size: 17px;
  }
  .front-contact .label { font-weight: 300; }
  .front-contact .email { font-weight: 700; }
  .front-base { position: absolute; left: 0; top: 659px; width: 530px; height: 27px; background: #1c1c1c; }

  /* Back */
  .back-header { position: absolute; left: 0; top: 0; width: 530px; height: 86px; background: var(--red); }
  .back-count { position: absolute; left: 33px; top: 6px; font-weight: 800; font-size: 72px; line-height: 1; text-shadow: 3px 3px 0 var(--black); }
  .back-title { position: absolute; left: 77px; top: 17px; font-weight: 800; font-size: 25px; line-height: 29px; text-shadow: 2px 2px 0 var(--black); letter-spacing: -0.2px; }

  .tip { position: absolute; left: 0; width: 530px; }
  .tip-number { position: absolute; left: 19px; top: 0; width: 18px; height: 18px; background: var(--red); font-size: 12px; line-height: 18px; text-align: center; }
  .tip-icon { position: absolute; left: 45px; top: -4px; width: 80px; height: 64px; }
  .tip-heading { position: absolute; left: 139px; top: 0; width: 370px; color: var(--red); font-weight: 700; font-size: 15px; line-height: 14px; }
  .tip-body { position: absolute; left: 139px; width: 370px; color: var(--body); font-size: 8.6px; line-height: 12.1px; }
  .tip-body strong { color: var(--white); font-weight: 700; }
  .divider { position: absolute; left: 18px; width: 494px; border-top: 1px dashed var(--rule); }

  .back-footer-mark { position: absolute; left: 0; top: 628px; width: 137px; height: 58px; background: var(--black); display: flex; align-items: center; justify-content: center; }
  .mini-lockup { display: inline-flex; align-items: center; gap: 5px; }
  .mini-mark { width: 18px; height: 18px; background: var(--red); }
  .mini-name { font-weight: 800; font-size: 19px; line-height: 1; }
  .back-contact {
    position: absolute; left: 137px; top: 628px; width: 393px; height: 58px; background: var(--red);
    display: flex; align-items: center; justify-content: center; gap: 5px; font-size: 13.5px;
  }
  .back-contact .label { font-weight: 300; }
  .back-contact .email { font-weight: 700; }
  .mail-icon { display: block; }
</style>
</head>
<body>

<section class="page front">
  <div class="brand">
    <div class="brand-lockup">
      <span class="brand-mark"></span>
      <span class="brand-name">THE LOFT</span>
    </div>
  </div>

  <svg class="burst" viewBox="0 0 140 100" role="img" aria-label="Starburst badge">
    <polygon points="70,0 82,18 104,8 102,30 132,30 114,48 140,66 108,70 110,96 86,82 70,100 56,82 26,92 32,70 0,62 24,46 8,26 38,28 38,6 58,18" fill="#ffffff" stroke="#0c0c0c" stroke-width="3"/>
  </svg>
  <p class="burst-label">SPECIAL<br>OFFER</p>

  <div class="offer offer-six">
    <div class="offer-frame"></div>
    <div class="offer-box">
      <p class="offer-lead offer-left">SIGN ON FOR</p>
      <p class="offer-big offer-left">6 MONTHS</p>
      <span class="offer-plus">+</span>
      <p class="offer-lead offer-right">GET YOUR FIRST</p>
      <p class="offer-big offer-right">6 WEEKS<br>FREE</p>
      <p class="offer-saving">SAVING OF <strong>$302</strong></p>
    </div>
  </div>

  <div class="offer offer-three">
    <div class="offer-frame"></div>
    <div class="offer-box">
      <p class="offer-lead offer-left">SIGN ON FOR</p>
      <p class="offer-big offer-left">3 MONTHS</p>
      <span class="offer-plus">+</span>
      <p class="offer-lead offer-right">GET YOUR FIRST</p>
      <p class="offer-big offer-right">3 WEEKS<br>FREE</p>
      <p class="offer-saving">SAVING OF <strong>$151</strong></p>
    </div>
  </div>

  <svg class="front-slash" viewBox="0 0 530 30" preserveAspectRatio="none">
    <polygon points="0,0 530,30 0,30" fill="#ec1c24"/>
  </svg>
  <div class="front-contact">
    <span class="label">CONTACT US:</span>
    <svg class="mail-icon" width="15" height="11" viewBox="0 0 15 11"><rect width="15" height="11" rx="1" fill="#fff"/><path d="M1 1.5 L7.5 6 L14 1.5" stroke="#ec1c24" stroke-width="1.5" fill="none"/></svg>
    <span class="email">THELOFTCANBERRA@MAILPINTO.COM</span>
  </div>
  <div class="front-base"></div>
</section>

<section class="page back">
  <header class="back-header">
    <span class="back-count">5</span>
    <h1 class="back-title">THINGS YOU CAN DO NOW TO LOOK<br>AFTER YOUR MENTAL HEALTH</h1>
  </header>

  <article class="tip" style="top:104px">
    <span class="tip-number">1</span>
    <svg class="tip-icon" viewBox="0 0 80 64">
      <path d="M30 14 h30 a12 12 0 0 1 12 12 v6 a12 12 0 0 1 -12 12 h-2 l6 9 l-14 -9 h-8 a12 12 0 0 1 -12 -12 v-6 a12 12 0 0 1 12 -12z" fill="#fff"/>
      <path d="M12 2 h34 a12 12 0 0 1 12 12 v6 a12 12 0 0 1 -12 12 h-24 l-12 8 l4 -8 a12 12 0 0 1 -12 -12 v-6 a12 12 0 0 1 12 -12z" fill="#fff" stroke="#181818" stroke-width="3"/>
      <rect x="12" y="10" width="30" height="3" fill="#181818"/><rect x="12" y="16" width="30" height="3" fill="#181818"/><rect x="12" y="22" width="30" height="3" fill="#181818"/>
    </svg>
    <h2 class="tip-heading">REMAIN CONNECTED TO SUPPORTIVE PEOPLE</h2>
    <p class="tip-body" style="top:18px">Spend time with and reach out to people who are a positive influence on you. Having a network of good relationships and taking part in social activities improves confidence, wellbeing and keeps our mind busy.</p>
  </article>
  <div class="divider" style="top:174px"></div>

  <article class="tip" style="top:193px">
    <span class="tip-number">2</span>
    <svg class="tip-icon" viewBox="0 0 80 64">
      <circle cx="40" cy="20" r="18" fill="#fff"/>
      <path d="M30 32 h20 v10 h-20z" fill="#fff"/>
      <rect x="30" y="45" width="20" height="4" rx="2" fill="#fff"/><rect x="31" y="51" width="18" height="4" rx="2" fill="#fff"/><rect x="35" y="57" width="10" height="4" rx="2" fill="#fff"/>
      <rect x="38" y="10" width="4" height="18" fill="#181818"/><rect x="31" y="17" width="18" height="4" fill="#181818"/>
    </svg>
    <h2 class="tip-heading">BE AWARE OF NEGATIVE THOUGHTS</h2>
    <p class="tip-body" style="top:18px">Thoughts arent necessarily facts and it can be easy to let our mind get away on us. Be aware of your negative thoughts and try not to give them power. Come up with a strategy so that when you notice yourself thinking negatively you can implement the strategy that overrides the thought, practice it regularly and overtime you’ll be the master of your mind, rather than your mind being the master of you!</p>
  </article>
  <div class="divider" style="top:284px"></div>

  <article class="tip" style="top:302px">
    <span class="tip-number">3</span>
    <svg class="tip-icon" viewBox="0 0 80 64">
      <path d="M38 4 c18 0 30 10 28 22 c-1 8 -12 6 -14 12 c-2 6 4 10 0 16 c-4 6 -14 8 -24 4 c-12 -5 -18 -16 -16 -28 c2 -14 12 -26 26 -26z" fill="#fff"/>
      <circle cx="26" cy="18" r="4" fill="#181818"/><circle cx="38" cy="12" r="4" fill="#181818"/><circle cx="51" cy="16" r="4" fill="#181818"/><circle cx="22" cy="32" r="4" fill="#181818"/><circle cx="30" cy="46" r="5" fill="#181818"/>
      <path d="M48 62 l22 -30" stroke="#fff" stroke-width="3"/><path d="M68 28 l6 -4 l-2 8z" fill="#fff"/>
    </svg>
    <h2 class="tip-heading">DEVELOP A DAILY ROUTINE THAT PRIORITISES<br>SOMETHING YOU ENJOY</h2>
    <p class="tip-body" style="top:31px"><strong>Make YOU your non negotiable.</strong> We all lead busy lives, but its important to do something for ourselves that we enjoy and can look forward to. Taking a bath, coffee with a friend, a walk, reading before bed, gardening. Its nice to look back on your day and see we have done something for ourselves.</p>
  </article>
  <div class="divider" style="top:398px"></div>

  <article class="tip" style="top:416px">
    <span class="tip-number">4</span>
    <svg class="tip-icon" viewBox="0 0 80 64" style="top:8px">
      <rect x="0" y="26" width="4" height="12" fill="#fff"/><rect x="6" y="14" width="8" height="36" rx="2" fill="#fff"/><rect x="16" y="8" width="8" height="48" rx="2" fill="#fff"/>
      <rect x="24" y="29" width="32" height="6" fill="#fff"/>
      <rect x="56" y="8" width="8" height="48" rx="2" fill="#fff"/><rect x="66" y="14" width="8" height="36" rx="2" fill="#fff"/><rect x="76" y="26" width="4" height="12" fill="#fff"/>
    </svg>
    <h2 class="tip-heading">EXERCISE, MOVEMENT IS KEY!</h2>
    <p class="tip-body" style="top:18px">Daily exercise is best however, its been proven that as little as 45 mins of exercise three times a week can lessen feelings of depressions, anxiety and stress. Find something you enjoy doing, a gym class where the session is planned for you, walk in do your exercise, walk out and get on with your day, walking, running, dancing, just be sure to get it done. The benefits are endless. Gradually build it into your routine, exercise with a friend, it helps keep you both accountable and its more fun too!</p>
  </article>
  <div class="divider" style="top:509px"></div>

  <article class="tip" style="top:530px">
    <span class="tip-number">5</span>
    <svg class="tip-icon" viewBox="0 0 80 64" style="top:2px">
      <path d="M14 4 l50 54" stroke="#fff" stroke-width="6" stroke-linecap="round"/>
      <path d="M12 2 l24 30 l-6 5z" fill="#fff"/>
      <path d="M16 60 l34 -38" stroke="#fff" stroke-width="6" stroke-linecap="round"/>
      <path d="M46 24 l10 -12 M50 28 l12 -12 M54 32 l12 -12 M46 26 l4 4 c6 4 12 -2 10 -8" stroke="#fff" stroke-width="3" fill="none" stroke-linecap="round"/>
    </svg>
    <h2 class="tip-heading">EAT WELL</h2>
    <p class="tip-body" style="top:18px">Our brain and gut are connected, this is known as the Gut Brain axis. Our GI tract releases neurotransmitters and hormones like serotonin and dopamine which affect brain function and mood. If the microbes in your gut are unbalanced it can lead to less production of the ‘happy hormones.’ Probiotics are key to balanced gut health, think probiotic yoghurts, kimchi, miso soup, sauerkraut or probiotic supplements. Vitamin D rich foods wil help too, eggs yolks, tuna, salmon. Lighten up on the sugary and processed food as these can inhibit the growth of good bacteria.</p>
  </article>

  <div class="back-footer-mark">
    <div class="mini-lockup"><span class="mini-mark"></span><span class="mini-name">THE LOFT</span></div>
  </div>
  <div class="back-contact">
    <span class="label">CONTACT US:</span>
    <svg class="mail-icon" width="12" height="9" viewBox="0 0 15 11"><rect width="15" height="11" rx="1" fill="#fff"/><path d="M1 1.5 L7.5 6 L14 1.5" stroke="#ec1c24" stroke-width="1.5" fill="none"/></svg>
    <span class="email">THELOFTCANBERRA@MAILPINTO.COM</span>
  </div>
</section>

</body>
</html>
```